Online Greeting Card Marketplace redesign

QuillPostly.com is a two-sided greeting card marketplace. Buyers purchase hand-made cards online, indicating their message. Sellers hand-write the message and mail directly to recipient.

We are getting decent foot traffic but low sales. I'm also not drawing a lot of Card Designers to sell their products. Feedback has been that it's cluttered, boring, and out of date.

I've always enjoyed vibes such as Dana Whitlock and Rosalind Perry. I was going for pale blues and chocolate browns (as can be seen in QuillPostly plain blue square and plain light blue square pages).

Attached document is my not-so-great attempt to redesign, which is uninviting and unpolished.

Need a new homepage and a second similar page when shopping (click on any category to see what I mean, e.g. Halloween).

Industry/Entity Type

Shopping

Requirements
Must have
• I think my logo (stick drawing of a man with an envelope) is what is currently driving a lot of traffic and should stay in the design, pending minor tweaks.

I'll need all the details of the final design to give to the programmers (font styles, color numbers, etc).

Nice to have
• I was thinking of a dotted frame to surround each picture? Frost Glimmer luminescent or a metallic? I just don't know if it works.

```html
<!DOCTYPE html>
<html lang="en">
<head>
<meta charset="utf-8">
<title>QuillPostly.com – Hand-Made Greeting Cards</title>
<link href="https://fonts.googleapis.com/css2?family=Cinzel:wght@400;700&family=EB+Garamond:wght@400;600;700&display=swap" rel="stylesheet">
<style>
:root{
  --page:#f3f3f3;
  --ink:#4a3a33;
  --brown:#4a342e;
  --brown-text:#6b4a1e;
  --blue:#0fb1e0;
  --blue-dark:#0b9cc8;
  --yellow:#f7d21e;
  --yellow-dark:#e6b514;
  --red:#c0392b;
  --grey:#d6d4d2;
  --muted:#7a7a7a;
  --white:#fff;
}
*{box-sizing:border-box;margin:0;padding:0}
html,body{width:1147px;height:1200px;overflow:hidden;background:var(--page)}
body{position:relative;font-family:"EB Garamond",Georgia,serif;color:var(--ink)}
.abs{position:absolute}

/* header */
.brand{left:168px;top:30px;width:372px;height:54px;border-bottom:1px solid var(--ink)}
.brand-name{font-size:27px;font-weight:400;color:var(--ink);letter-spacing:.5px;display:flex;align-items:center;gap:10px}
.brand-dot{width:14px;height:14px;border-radius:50%;background:var(--blue)}
.brand-tag{font-size:12px;margin-left:118px;margin-top:2px}
.brand-tag i{color:var(--red);font-style:normal;margin:0 4px}
.account{left:612px;top:46px;display:flex;align-items:center;font-size:13.5px;gap:10px}
.account .seller{background:var(--blue);color:var(--white);padding:2px 15px}
.account .sep{color:var(--muted)}
.cart{display:flex;align-items:center;gap:6px}
.cart b{font-family:Arial,sans-serif}

/* nav ribbon */
.ribbon-end{top:126px;width:44px;height:52px;background:var(--yellow-dark)}
.ribbon-end.l{left:122px;clip-path:polygon(0 0,100% 0,100% 100%,0 100%,40% 50%)}
.ribbon-end.r{left:982px;clip-path:polygon(0 0,100% 0,60% 50%,100% 100%,0 100%)}
.nav{left:156px;top:113px;width:835px;height:49px;background:var(--yellow);display:flex;align-items:center;padding-left:24px;box-shadow:0 2px 2px rgba(0,0,0,.15)}
.nav a{color:var(--brown-text);font-weight:700;font-size:13.5px;text-decoration:none}
.nav .dot{color:var(--red);margin:0 16px;font-size:12px}
.search{position:absolute;right:20px;top:10px;width:183px;height:26px;border-radius:13px;background:var(--white);border:1px solid var(--yellow-dark)}
.search svg{position:absolute;right:10px;top:5px}

/* steps */
.steps{left:168px;top:162px;width:808px;height:76px;background:var(--blue);color:var(--white);font-size:17.5px}
.step-choose{position:absolute;left:0;top:0;width:256px;height:76px;background:var(--brown);clip-path:polygon(0 0,95% 0,100% 50%,95% 100%,0 100%)}
.step{position:absolute;top:27px}
.step-divider{position:absolute;left:462px;top:0;height:76px;width:14px}

/* featured */
.feature{top:265px;width:263px;height:216px;border:1px dotted var(--blue);padding:9px}
.feature div{width:100%;height:100%}

/* sections */
.heading{left:166px;font-family:Cinzel,serif;font-weight:700;color:var(--blue);font-size:30px;font-variant:small-caps;letter-spacing:.3px}
.arrow{width:28px;height:48px;background:var(--grey);display:flex;align-items:center;justify-content:center}
.card{width:152px;height:189px;background:var(--white);border:1px dotted var(--blue);text-align:center;box-shadow:0 6px 5px -5px rgba(0,0,0,.25)}
.card.active{background:linear-gradient(var(--white),#f1d9cd 20%,#e4b8a5);border:1px solid #d6a894}
.card .art{margin:20px auto 0;width:78px;height:100px}
.card .art.wide{width:96px;height:80px;margin-top:28px}
.card h3{font-weight:400;font-size:14px;margin-top:16px;line-height:1}
.card .art.wide + h3{margin-top:28px}
.card p{font-size:10px;color:var(--muted);margin-top:3px}
.art-halloween{background:linear-gradient(#9a9c9b,#c58468)}
.art-veteran{background:linear-gradient(#b9d6ec,#6d7f8c)}
.art-columbus{background:linear-gradient(#ffffff,#dcecf3)}
.art-mothers{background:linear-gradient(#6a2230,#d9506c)}
.art-grand{background:linear-gradient(#8fbcaa,#d39a98)}

/* newsletter */
.newsletter{left:168px;top:1094px;width:808px;height:50px;background:var(--yellow);display:flex;align-items:center;padding-left:22px}
.newsletter h2{font-size:23px;font-weight:600;color:var(--brown-text);margin-left:14px}
.newsletter .field{position:absolute;left:427px;top:12px;width:214px;height:25px;border-radius:13px;background:var(--white);border:1px solid var(--yellow-dark)}
.newsletter .subscribe{position:absolute;left:656px;top:12px;width:134px;height:25px;border-radius:13px;background:var(--red);color:var(--white);font-weight:700;font-size:16px;text-align:center;line-height:25px}

.footer{left:168px;top:1160px;font-size:11.5px}
.footer span{color:var(--muted);margin:0 7px}
.follow{left:838px;top:1163px;font-size:11px}
.social{top:1156px;width:26px;height:25px}
</style>
</head>
<body>

<header>
  <div class="abs brand">
    <div class="brand-name"><span class="brand-dot"></span>QuillPostly.com</div>
    <div class="brand-tag">Hand~Made<i>•</i>Hand~Written<i>•</i>Hand~Delivered</div>
  </div>
  <div class="abs account">
    <span class="seller">Sellers Sign In</span><span class="sep">|</span>
    <span>Customer Sign In</span><span class="sep">|</span>
    <span class="cart">CART
      <svg width="17" height="14" viewBox="0 0 17 14"><path d="M0 1h3l2 8h9l2-6H4" fill="none" stroke="#4a3a33" stroke-width="1.6"/><circle cx="6" cy="12" r="1.5" fill="#4a3a33"/><circle cx="13" cy="12" r="1.5" fill="#4a3a33"/></svg>
      <b>(0)</b></span>
  </div>
</header>

<div class="abs ribbon-end l"></div>
<div class="abs ribbon-end r"></div>
<nav class="abs nav">
  <a>UP COMING HOLIDAYS</a><span class="dot">•</span>
  <a>EVERYDAY CARDS</a><span class="dot">•</span>
  <a>BIRTHDAYS</a><span class="dot">•</span>
  <a>ALL CATEGORIES</a>
  <div class="search"><svg width="15" height="15" viewBox="0 0 15 15"><circle cx="6" cy="6" r="4.8" fill="none" stroke="#666" stroke-width="1.6"/><path d="M9.5 9.5L14 14" stroke="#666" stroke-width="2"/></svg></div>
</nav>

<section class="abs steps">
  <div class="step-choose"></div>
  <span class="step" style="left:21px">STEP 1: CHOOSE A CARD</span>
  <span class="step" style="left:274px">STEP 1: CUSTOMIZE IT</span>
  <svg class="step-divider" viewBox="0 0 14 76" preserveAspectRatio="none"><path d="M1 0L13 38L1 76" fill="none" stroke="#0b9cc8" stroke-width="1.5"/></svg>
  <span class="step" style="left:499px">STEP 1: WE HANDWRITE AND MAIL</span>
</section>

<div class="abs feature" style="left:166px"><div role="img" aria-label="Chalkboard card with a beehive and the words you are so sweet" style="background:linear-gradient(135deg,#3a3a3a,#222)"></div></div>
<div class="abs feature" style="left:442px"><div role="img" aria-label="Illustrated card of a blue bird on a flowering branch" style="background:linear-gradient(135deg,#f8ee9c,#f2e07a)"></div></div>
<div class="abs feature" style="left:717px"><div role="img" aria-label="Handmade card of a floral baby pram" style="background:linear-gradient(135deg,#f4f1ee,#9fdcd0 60%,#e9e4de)"></div></div>

<h2 class="abs heading" style="top:510px">Upcoming Holidays</h2>
<div class="abs arrow" style="left:142px;top:642px"><svg width="9" height="14"><path d="M7 1L2 7l5 6" fill="none" stroke="#fff" stroke-width="2"/></svg></div>
<div class="abs arrow" style="left:977px;top:642px"><svg width="9" height="14"><path d="M2 1l5 6-5 6" fill="none" stroke="#fff" stroke-width="2"/></svg></div>

<div class="abs card" style="left:168px;top:572px"><div class="art art-halloween" role="img" aria-label="Happy Halloween tombstone card"></div><h3>Halloween</h3><p>By - Quill Postly</p></div>
<div class="abs card active" style="left:333px;top:572px"><div class="art art-veteran" role="img" aria-label="Paper-cut sailboat card for Veteran's Day"></div><h3>Veteran's Day</h3><p>By - Quill Postly</p></div>
<div class="abs card" style="left:498px;top:572px"><div class="art art-columbus" role="img" aria-label="Stitched sailboat card for Columbus Day"></div><h3>Columbus Day</h3><p>By - Quill Postly</p></div>
<div class="abs card" style="left:662px;top:572px"><div class="art art-mothers" role="img" aria-label="Thanks Mom card with a pink tulip"></div><h3>Mothers Day</h3><p>By - Quill Postly</p></div>
<div class="abs card" style="left:826px;top:572px"><div class="art wide art-grand" role="img" aria-label="Floral grandmother card"></div><h3>Mothers Day</h3><p>By - Quill Postly</p></div>

<h2 class="abs heading" style="top:788px">New Card</h2>
<div class="abs arrow" style="left:142px;top:921px"><svg width="9" height="14"><path d="M7 1L2 7l5 6" fill="none" stroke="#fff" stroke-width="2"/></svg></div>
<div class="abs arrow" style="left:977px;top:921px"><svg width="9" height="14"><path d="M2 1l5 6-5 6" fill="none" stroke="#fff" stroke-width="2"/></svg></div>

<div class="abs card" style="left:168px;top:851px"><div class="art art-halloween" role="img" aria-label="Happy Halloween tombstone card"></div><h3>Halloween</h3><p>By - Quill Postly</p></div>
<div class="abs card" style="left:333px;top:851px"><div class="art art-veteran" role="img" aria-label="Paper-cut sailboat card for Veteran's Day"></div><h3>Veteran's Day</h3><p>By - Quill Postly</p></div>
<div class="abs card" style="left:498px;top:851px"><div class="art art-columbus" role="img" aria-label="Stitched sailboat card for Columbus Day"></div><h3>Columbus Day</h3><p>By - Quill Postly</p></div>
<div class="abs card" style="left:662px;top:851px"><div class="art art-mothers" role="img" aria-label="Thanks Mom card with a pink tulip"></div><h3>Mothers Day</h3><p>By - Quill Postly</p></div>
<div class="abs card" style="left:826px;top:851px"><div class="art wide art-grand" role="img" aria-label="Floral grandmother card"></div><h3>Mothers Day</h3><p>By - Quill Postly</p></div>

<section class="abs newsletter">
  <svg width="30" height="20" viewBox="0 0 30 20"><rect x="1" y="1" width="28" height="18" fill="none" stroke="#4a342e" stroke-width="2"/><path d="M1 1l14 11L29 1M1 19l10-9M29 19l-10-9" fill="none" stroke="#4a342e" stroke-width="1.6"/></svg>
  <h2>Sign up to our NEWSLETTER</h2>
  <div class="field"></div>
  <div class="subscribe">SUBSCRIBE</div>
</section>

<footer>
  <div class="abs footer">Home<span>|</span>About Us<span>|</span>FAQ'S<span>|</span>Contact Us<span>|</span>Copyrights © 2011-2013, QuillPostly.com</div>
  <div class="abs follow">FOLLOW US</div>
  <div class="abs social" style="left:925px;background:#4a7fd1" aria-label="Social page"></div>
  <div class="abs social" style="left:951px;background:#5bc0ec" aria-label="Social page"></div>
</footer>

</body>
</html>
```